Small but growing painting company. Have built up a steady client base. Want to start having a more professional look. Want to start with changing my business cards, and also getting new logo and tee shirts.

Target Market(s)

Home owners, property management companies, all ages 30-70

Industry/Entity Type

Painting And Decorating

Contact Information for Business Card

Bright Ridge Painting LLC Mark Delvecchi 630-584-3907 interior, exterior, vaulted ceiling, drywall repair, pressure washing, kitchen cabinets, epoxy, garage floors,

Font styles to use
Sans Serif
Other font styles liked:
• Harrington

Colors
0355a3
ffffff
ec1f27
000000
3176b5
0493ce
474747
b7b7b7

Requirements
Must have
• Creative, something that doesn’t look like every other painting card.
Nice to have
• I would like something with an arrow or something going to a point

```html
<!DOCTYPE html>
<html lang="en">
<head>
<meta charset="utf-8">
<title>Bright Ridge Painting LLC – Business Card</title>
<link href="https://fonts.googleapis.com/css2?family=Montserrat:wght@400;500;700&family=Satisfy&display=swap" rel="stylesheet">
<style>
  :root {
    --page-bg: #eef0f1;
    --card-white: #ffffff;
    --band-blue: #4aa6dd;
    --brand-blue: #2f95d6;
    --title-orange: #f08a2c;
    --ink: #3a3a3a;
    --white: #ffffff;
  }
  html, body {
    margin: 0;
    width: 1200px;
    height: 1200px;
    overflow: hidden;
    background: var(--page-bg);
  }
  .business-card {
    position: absolute;
    left: 100px;
    top: 314px;
    width: 1000px;
    height: 572px;
    background: var(--card-white);
    box-shadow: 0 10px 30px rgba(0,0,0,0.12);
    overflow: hidden;
    font-family: "Montserrat", Arial, sans-serif;
  }
  .card-art {
    position: absolute;
    inset: 0;
  }
  .company-name {
    position: absolute;
    left: 520px;
    top: 92px;
    width: 440px;
    text-align: right;
    font-size: 34px;
    font-weight: 700;
    color: var(--brand-blue);
    letter-spacing: 0.5px;
  }
  .holder {
    position: absolute;
    left: 170px;
    top: 140px;
  }
  .holder-name {
    font-size: 26px;
    font-weight: 700;
    letter-spacing: 2px;
    text-transform: uppercase;
    color: var(--brand-blue);
  }
  .holder-title {
    margin-top: 4px;
    padding-left: 60px;
    font-size: 24px;
    font-weight: 400;
    color: var(--title-orange);
  }
  .services {
    position: absolute;
    left: 60px;
    top: 268px;
    width: 490px;
    font-family: "Satisfy", cursive;
    font-size: 22px;
    line-height: 1.45;
    color: var(--white);
  }
  .contact-list {
    position: absolute;
    left: 618px;
    top: 238px;
    margin: 0;
    padding: 0;
    list-style: none;
    font-size: 23px;
    font-weight: 500;
    line-height: 1.5;
    color: var(--ink);
  }
</style>
</head>
<body>
  <article class="business-card">
    <svg class="card-art" viewBox="0 0 1000 572" width="1000" height="572" aria-hidden="true">
      <path class="brush-band" fill="var(--band-blue)"
        d="M0,238 L30,230 L70,242 L110,228 L160,238 L205,226 L250,240 L300,229 L350,237 L400,225 L445,236 L490,226 L540,234 L560,224
           L600,224 L600,372 Q600,394 622,394 L1000,394 L1000,572 L0,572 Z"/>
      <g class="contact-icons" fill="none" stroke="var(--white)" stroke-width="2.4" stroke-linecap="round" stroke-linejoin="round">
        <rect x="572" y="244" width="15" height="24" rx="3"/>
        <line x1="577" y1="263" x2="582" y2="263"/>
        <rect x="569" y="286" width="22" height="15" rx="2"/>
        <polyline points="569,287 580,296 591,287"/>
        <path d="M580,346 C572,336 571,330 571,327 A9,9 0 0 1 589,327 C589,330 588,336 580,346 Z"/>
        <circle cx="580" cy="327" r="3"/>
      </g>
    </svg>

    <div class="company-name">Bright Ridge Painting LLC</div>

    <div class="holder">
      <div class="holder-name">Mark Delvecchi</div>
      <div class="holder-title">CEO/Founder</div>
    </div>

    <p class="services">Interior, Exterior, Vaulted Ceiling, Drywall Repair,<br>Pressure Washing, Kitchen Cabinets, Epoxy, Garage Floors</p>

    <ul class="contact-list">
      <li>630-584-3907</li>
      <li>mdelvecchi@brightridge.com</li>
      <li>Harlow Lane 7, 2604<br>Melbourne.</li>
    </ul>
  </article>
</body>
</html>
```